Stress Fracture Infographic for Scientific Paper

We need an infographic for a research/scientific paper. We would like the infographic to give readers a clear and eye-catching overview about the factors that put athletes and military personnel at risk for stress fractures. The design needs to communicate that the risk factors are cumulative and interactive; however, how they specifically accumulate and interact has not been studied or shown in the literature (we need healthcare providers who subjectively assess cumulative risk profiles in athletes and we concurrently need scientists to evaluate the interdependence of risk factors). We define cumulative risk profile as: a subjective clinical determination of the number of factors putting an athlete at risk along with thoughtful consideration regarding how all the risk factors interact with one another. We would like the infographic to display this cumulative risk profile idea.

The risk factors can be categorized as:
INTRINSIC-
Non-modifiable (such as sex, race, age, genetics, anatomical structure, and prior bone stress injury), modifiable (muscle strength, muscle fatigue, flexibility, biomechanics, stress, recovery strategies, nutrition, energy deficiency), unclear if modifiable, not, or somewhere in between (such as gut health);

EXTRINSIC-
Modifiable (footwear, training surface, workload)

Target Market(s)

Researchers and clinicians

Requirements
Must have
• A scientific feel
Nice to have
• Creative way to display the cumulative and interactive impact of risk factors
Should not have
• Too cartoon-ish or child-like feel

```html
<!DOCTYPE html>
<html lang="en">
<head>
<meta charset="utf-8">
<title>Stress Fracture Cumulative Risk Profile</title>
<link href="https://fonts.googleapis.com/css2?family=Arimo:wght@700&family=Montserrat:wght@700&display=swap" rel="stylesheet">
<style>
  :root {
    --bg: #ffffff;
    --field: #bde5f7;
    --intrinsic-soft: #96d4f0;
    --intrinsic-mid: #7ccbee;
    --core: #27a3dd;
    --extrinsic-soft: #b3dfc4;
    --blue-text: #0a6db5;
    --green-text: #0d8d40;
    --grey-text: #454545;
    --arrow: #666666;
    --heat: #fdb98a;
  }
  html, body {
    margin: 0;
    padding: 0;
    width: 1200px;
    height: 1200px;
    overflow: hidden;
    background: var(--bg);
  }
  .infographic { display: block; width: 1200px; height: 1200px; }
  .title { font-family: "Arimo", Arial, sans-serif; font-weight: 700; font-size: 30px; }
  .title--intrinsic { fill: var(--blue-text); }
  .title--extrinsic { fill: var(--green-text); }
  .group-heading { font-family: "Arimo", Arial, sans-serif; font-weight: 700; font-size: 20px; }
  .group-items { font-family: "Arimo", Arial, sans-serif; font-weight: 700; font-size: 14.5px; }
  .blue { fill: var(--blue-text); }
  .green { fill: var(--green-text); }
  .risk-label { font-family: "Montserrat", Arial, sans-serif; font-weight: 700; font-size: 23px; fill: var(--grey-text); }
</style>
</head>
<body>
<svg class="infographic" viewBox="0 0 1200 1200" xmlns="http://www.w3.org/2000/svg">
  <defs>
    <clipPath id="field-clip"><circle cx="597.5" cy="530" r="311"/></clipPath>
    <radialGradient id="heat-glow" cx="0.5" cy="0.5" r="0.5">
      <stop offset="0" stop-color="var(--heat)" stop-opacity="1"/>
      <stop offset="0.55" stop-color="var(--heat)" stop-opacity="0.8"/>
      <stop offset="1" stop-color="var(--heat)" stop-opacity="0"/>
    </radialGradient>
  </defs>

  <!-- risk field -->
  <circle class="risk-field" cx="597.5" cy="530" r="311" fill="var(--field)"/>

  <!-- athlete area -->
  <g clip-path="url(#field-clip)">
    <ellipse class="athlete-area" role="img" aria-label="Illustration of a running athlete silhouette with highlighted stress fracture sites at hip, thigh, shin and foot"
      cx="600" cy="730" rx="215" ry="190" fill="url(#heat-glow)"/>
  </g>

  <!-- factor groups -->
  <ellipse class="group group--nonmod" cx="481" cy="392" rx="125" ry="70" transform="rotate(10 481 392)" fill="var(--intrinsic-soft)" fill-opacity="0.75"/>
  <ellipse class="group group--extrinsic" cx="516" cy="508" rx="119" ry="81" transform="rotate(-22 516 508)" fill="var(--extrinsic-soft)" fill-opacity="0.85"/>
  <ellipse class="group group--mod" cx="687" cy="389" rx="139" ry="94" fill="var(--intrinsic-soft)" fill-opacity="0.6"/>
  <ellipse class="group group--unclear" cx="661" cy="470" rx="97" ry="44" transform="rotate(10 661 470)" fill="var(--intrinsic-mid)" fill-opacity="0.7"/>
  <ellipse class="group-core" cx="584" cy="437" rx="15" ry="9" transform="rotate(-30 584 437)" fill="var(--core)"/>

  <!-- arrow -->
  <path class="risk-arrow" d="M689 552 C640 515 605 480 589 442" fill="none" stroke="var(--arrow)" stroke-width="1.5"/>
  <path class="risk-arrowhead" d="M587 438 L594 451 L590 448 L584 450 Z" fill="var(--arrow)"/>

  <!-- titles -->
  <text class="title title--intrinsic" text-anchor="middle" dominant-baseline="central">
    <tspan x="541" y="275">Intrinsic</tspan><tspan x="541" y="302">Factors</tspan>
  </text>
  <text class="title title--extrinsic" text-anchor="end" dominant-baseline="central">
    <tspan x="444" y="600">Extrinsic</tspan><tspan x="444" y="627">Factors</tspan>
  </text>

  <!-- non-modifiable -->
  <text class="group-heading blue" x="466" y="357" text-anchor="middle" dominant-baseline="central">Non-Modifiable</text>
  <text class="group-items blue" text-anchor="middle" dominant-baseline="central">
    <tspan x="466" y="383">Sex :  Race : Age :</tspan>
    <tspan x="466" y="405">Genetics : Alignment :</tspan>
    <tspan x="466" y="427">Prior Injury</tspan>
  </text>

  <!-- intrinsic modifiable -->
  <text class="group-heading blue" x="700" y="326" text-anchor="middle" dominant-baseline="central">Modifiable</text>
  <text class="group-items blue" text-anchor="middle" dominant-baseline="central">
    <tspan x="700" y="355">Strength : Fatigue :</tspan>
    <tspan x="700" y="377">Flexibility : Biomechanics :</tspan>
    <tspan x="700" y="399">Stress : Recovery :</tspan>
    <tspan x="700" y="420">Vit D : REDs</tspan>
  </text>

  <!-- unclear -->
  <text class="group-heading blue" x="636" y="461" dominant-baseline="central">Unclear</text>
  <text class="group-items blue" x="637" y="486" dominant-baseline="central">Gut Health</text>

  <!-- extrinsic modifiable -->
  <text class="group-heading green" x="517" y="493" text-anchor="middle" dominant-baseline="central">Modifiable</text>
  <text class="group-items green" text-anchor="middle" dominant-baseline="central">
    <tspan x="520" y="516">Footwear : Training Surface :</tspan>
    <tspan x="520" y="537">Workload</tspan>
  </text>

  <!-- cumulative risk -->
  <text class="risk-label" dominant-baseline="central">
    <tspan x="679" y="572">Cumulative</tspan><tspan x="679" y="597">Risk Profile</tspan>
  </text>
</svg>
</body>
</html>
```